Advertising brochure for Trail Along Southside

We need a new single sided DL flier for the 2020 season!<br/>This flier is for our tour business. You can find all the details about the tour at our web site http://trailalong.southside.example<br/>The flier needs to grab the tourists attention, explain the tour and give price. I will upload a copy of last year's flier for your reference.<br/>We'd like the flier to match our web site to some extent.<br/>The most up to date information is on the web site and NOT last year's brochure. Use the web site for tour itinerary. We NO LONGER do the "Orchard Walk".<br/>Remember the size is "DL". Please no A4 format etc.<br/>You will be able to source images from:<br/>- Our web site<br/>- Our Chatterbook<br/>- Roamreview<br/>- Quarrel Listings<br/>If you have a particular idea in mind then feel free to contact us and we will try to accommodate your photo request.<br/>Good luck!

Target Market(s)

All ages

Industry/Entity Type

Tourism

Requirements
Must have
• Phone number
• Web Site
• Email address
• Price
Nice to have
• Description of tour and images

```html
<!DOCTYPE html>
<html lang="en">
<head>
<meta charset="utf-8">
<title>Trail Along Southside – Tour Flier</title>
<link href="https://fonts.googleapis.com/css2?family=Poppins:ital,wght@0,400;0,500;0,600;0,700;0,800;1,300;1,400;1,800&display=swap" rel="stylesheet">
<style>
  :root {
    --orange: #ff6a0d;
    --orange-soft: #ffa35c;
    --paper: #f8f8f8;
    --ink: #222222;
    --backdrop: #e9e9e9;
    --white: #ffffff;
  }
  * { box-sizing: border-box; margin: 0; padding: 0; }
  html, body { width: 1200px; height: 1143px; overflow: hidden; }
  body {
    background: var(--backdrop);
    font-family: "Poppins", Arial, sans-serif;
    position: relative;
  }
  .flier {
    position: absolute;
    left: 345px; top: 31px;
    width: 510px; height: 1080px;
    background: var(--paper);
    overflow: hidden;
    box-shadow: 0 4px 18px rgba(0,0,0,.12);
  }
  .masthead {
    position: absolute; left: 0; top: 0; width: 510px; height: 224px;
    background: var(--orange);
  }
  .brand-name {
    position: absolute; left: 52px; top: 58px;
    color: var(--white); font-weight: 600; font-size: 40px; line-height: 40px;
    letter-spacing: -0.5px;
  }
  .brand-rule {
    position: absolute; left: 52px; top: 155px; width: 295px; height: 2px; background: var(--white);
  }
  .brand-region {
    position: absolute; left: 48px; top: 160px;
    color: var(--white); font-weight: 600; font-size: 44px; line-height: 52px; letter-spacing: -1px;
  }
  .tile {
    position: absolute; border: 1.5px solid var(--orange); background: var(--paper);
    padding: 9px 6px 6px 5px;
  }
  .tile h2 {
    color: var(--orange); font-weight: 500; font-size: 17.5px; line-height: 21px; text-transform: uppercase;
    white-space: nowrap;
  }
  .tile p {
    color: var(--ink); font-style: italic; font-weight: 300; font-size: 10.5px; line-height: 13px;
    margin-top: 14px;
  }
  .photo { position: absolute; }
  .photo--dugout { background: linear-gradient(135deg, #b99a8a 0%, #8d6b5c 45%, #c9a48d 70%, #5b4b7c 100%); }
  .photo--mine { background: linear-gradient(180deg, #a8c4cc 0%, #b5c8cb 45%, #b98b6e 62%, #7c5a44 100%); }
  .photo--drive { background: linear-gradient(160deg, #c9bcae 0%, #ddd2c5 50%, #b6a892 100%); }
  .photo--opal { background: radial-gradient(ellipse 40% 22% at 52% 52%, #7a5a2e 0%, #4e3a28 60%, #f4f4f4 100%); }
  .photo--framed { border: 1.5px solid var(--orange); }
  .contact { position: absolute; left: 47px; top: 983px; }
  .contact-phone {
    display: flex; align-items: center; gap: 8px;
    color: var(--orange); font-weight: 800; font-size: 26px; line-height: 30px;
  }
  .contact-line {
    display: flex; align-items: center; gap: 14px; margin-top: 6px;
    color: var(--orange); font-style: italic; font-size: 11px; line-height: 12px;
  }
  .contact-line svg { flex: none; }
  .price-badge { position: absolute; left: 335px; top: 890px; }
  .price-amount {
    position: absolute; left: 359px; top: 945px; width: 140px; text-align: center;
    color: var(--white); font-weight: 800; font-style: italic; font-size: 54px; line-height: 56px;
  }
  .price-unit {
    position: absolute; left: 359px; top: 1003px; width: 140px; text-align: center;
    color: var(--white); font-style: italic; font-size: 14px; letter-spacing: 2.5px;
  }
  .price-note {
    position: absolute; left: 369px; top: 1033px; width: 120px; text-align: center;
    color: var(--white); font-weight: 700; font-size: 8.5px; line-height: 11px;
  }
  .footer-band { position: absolute; left: 0; bottom: 0; width: 510px; height: 19px; background: var(--orange); }
</style>
</head>
<body>
<main class="flier">
  <header class="masthead">
    <div class="brand-name">Trail Along</div>
    <div class="brand-rule"></div>
    <div class="brand-region">SOUTHSIDE</div>
  </header>

  <section class="tile" style="left:47px;top:235px;width:151px;height:156px;">
    <h2>Visit a modern<br>underground<br>dugout</h2>
    <p>Step inside our underground home and see how a modern family lives in Ridgecrest.</p>
  </section>
  <div class="photo photo--dugout" style="left:204px;top:235px;width:257px;height:156px;" role="img" aria-label="Photo of a bedroom inside an underground dugout home"></div>

  <div class="photo photo--mine" style="left:48px;top:396px;width:258px;height:157px;" role="img" aria-label="Photo of an old opal mining truck among spoil heaps"></div>
  <section class="tile" style="left:312px;top:396px;width:149px;height:157px;">
    <h2>Visit an opal<br>mine</h2>
    <p>Get a unique insight into opal mining as we show you how a real opal mine operates.</p>
  </section>

  <section class="tile" style="left:47px;top:559px;width:151px;height:156px;padding-left:9px;">
    <h2>A scenic drive<br>through the<br>field</h2>
    <p>View the magnificent scenery that over 100 years of terraforming has created from the comfort of your own car.</p>
  </section>
  <div class="photo photo--drive" style="left:204px;top:559px;width:257px;height:156px;" role="img" aria-label="Aerial photo of cars driving through the opal fields"></div>

  <div class="photo photo--opal photo--framed" style="left:47px;top:720px;width:259px;height:157px;" role="img" aria-label="Photo of a polished boulder opal"></div>
  <section class="tile" style="left:312px;top:720px;width:149px;height:157px;padding-left:12px;">
    <h2>Noodling<br>for opal</h2>
    <p>Now it's time to find your very own opal by fossicking (noodling) for your own. Our expert guide will show you how it's done.</p>
  </section>

  <div class="contact">
    <div class="contact-phone">
      <svg width="26" height="26" viewBox="0 0 24 24" aria-hidden="true"><path d="M6.6 10.8a15 15 0 0 0 6.6 6.6l2.2-2.2c.3-.3.7-.4 1-.2 1.1.4 2.3.6 3.6.6.6 0 1 .4 1 1V20c0 .6-.4 1-1 1A17 17 0 0 1 3 4c0-.6.4-1 1-1h3.5c.6 0 1 .4 1 1 0 1.3.2 2.5.6 3.6.1.3 0 .7-.2 1z" fill="#ff6a0d"/><path d="M14 3a7 7 0 0 1 7 7M14 6.5a3.5 3.5 0 0 1 3.5 3.5" stroke="#ff6a0d" stroke-width="1.8" fill="none" stroke-linecap="round"/></svg>
      <span>08 5550 1274</span>
    </div>
    <div class="contact-line">
      <svg width="12" height="9" viewBox="0 0 12 9" aria-hidden="true"><rect width="12" height="9" rx="1" fill="#ff6a0d"/><path d="M0.5 0.8 6 5 11.5 0.8" stroke="#f8f8f8" stroke-width="1.1" fill="none"/></svg>
      <span>hello@trailalong.southside.example</span>
    </div>
    <div class="contact-line">
      <svg width="12" height="12" viewBox="0 0 12 12" aria-hidden="true"><circle cx="6" cy="6" r="5.5" fill="#ff6a0d"/><path d="M0.5 6h11M6 .5c-2.5 3-2.5 8 0 11M6 .5c2.5 3 2.5 8 0 11" stroke="#f8f8f8" stroke-width=".8" fill="none"/></svg>
      <span>www.trailalong.southside.example</span>
    </div>
  </div>

  <svg class="price-badge" width="190" height="190" viewBox="0 0 190 190" aria-hidden="true">
    <circle cx="95" cy="96" r="80" fill="#ff6a0d"/>
    <path d="M22 130 A85 85 0 0 1 60 18" stroke="#ff6a0d" stroke-width="3" fill="none"/>
    <path d="M70 10 A88 88 0 0 1 122 10" stroke="#ff6a0d" stroke-width="4" fill="none" stroke-linecap="round"/>
    <path d="M58 38 A70 70 0 0 1 132 38" stroke="#ffffff" stroke-width="3" fill="none" stroke-linecap="round"/>
    <path d="M180 110 A86 86 0 0 1 150 170" stroke="#ff6a0d" stroke-width="3" fill="none"/>
  </svg>
  <div class="price-amount">40$</div>
  <div class="price-unit">PER PERSON</div>
  <div class="price-note">kids half and children<br>under 5 free</div>

  <div class="footer-band"></div>
</main>
</body>
</html>
```